Startup incubator requires a funky cool brochure

please see design brief, please be creative but within the design confines listed in the corporatedesign pdf file

Industry/Entity Type

Startup

```html
<!DOCTYPE html>
<html lang="en">
<head>
<meta charset="utf-8">
<title>Liftoff Startup Hub – Landing Gear</title>
<link href="https://fonts.googleapis.com/css2?family=Questrial&family=Cutive+Mono&display=swap" rel="stylesheet">
<style>
  :root {
    --orange: #f8b000;
    --orange-mid: #f9c24d;
    --orange-soft: #fbd77e;
    --orange-pale: #fde6b3;
    --ink: #616161;
    --paper: #ffffff;
  }
  html, body {
    margin: 0;
    padding: 0;
    overflow: hidden;
    background: var(--paper);
  }
  .brochure-cover {
    position: relative;
    width: 848px;
    height: 1200px;
    overflow: hidden;
    background: var(--paper);
    font-family: "Questrial", "Century Gothic", sans-serif;
  }
  .cover-art {
    position: absolute;
    inset: 0;
  }
  .tile { fill: var(--orange); opacity: 0.58; }
  .tile--pale { fill: var(--orange); opacity: 0.28; }

  .brand {
    position: absolute;
    left: 488px;
    top: 276px;
    width: 345px;
    text-align: center;
    color: var(--orange);
  }
  .brand__name {
    font-size: 60px;
    line-height: 64px;
    letter-spacing: 10px;
    margin-right: -10px;
  }
  .brand__tagline {
    font-size: 16px;
    letter-spacing: 5.2px;
    margin-top: 6px;
  }

  .quote {
    position: absolute;
    left: 0;
    top: 0;
    margin: 0;
    color: var(--ink);
  }
  .quote__line {
    position: absolute;
    display: flex;
    align-items: baseline;
    white-space: nowrap;
    gap: 14px;
  }
  .quote__small { font-size: 35px; }
  .quote__large { font-size: 74px; line-height: 1; }
  .quote__mid { font-size: 44px; letter-spacing: 1px; }
  .quote__hero { font-size: 80px; line-height: 1; letter-spacing: 2px; }
  .quote__mark {
    color: var(--orange);
    font-size: 46px;
    font-family: Georgia, serif;
  }
  .line-1 { left: 212px; top: 452px; }
  .line-2 { left: 236px; top: 518px; }
  .line-3 { left: 232px; top: 598px; }
  .line-4 { left: 306px; top: 648px; }

  .attribution {
    position: absolute;
    left: 300px;
    top: 732px;
    width: 280px;
    text-align: center;
    font-family: "Cutive Mono", monospace;
    font-size: 23px;
    line-height: 38px;
    color: var(--orange);
    margin: 0;
  }
</style>
</head>
<body>
<main class="brochure-cover">
  <svg class="cover-art" width="848" height="1200" viewBox="0 0 848 1200" aria-hidden="true">
    <path d="M155,392 Q470,150 848,125 L848,0 L155,0 Z" fill="var(--orange-pale)"/>
    <path d="M155,345 Q430,70 760,0 L155,0 Z" fill="var(--orange-soft)"/>
    <path d="M155,272 Q330,70 560,0 L155,0 Z" fill="var(--orange-mid)"/>
    <path d="M155,186 Q250,60 365,0 L155,0 Z" fill="var(--orange)"/>
    <rect class="side-band" x="0" y="0" width="156" height="1200" fill="var(--orange)"/>

    <g class="tiles">
      <rect class="tile" x="808" y="460" width="60" height="58" rx="9"/>
      <rect class="tile" x="778" y="540" width="46" height="35" rx="5"/>
      <rect class="tile" x="732" y="598" width="54" height="40" rx="6"/>
      <rect class="tile" x="760" y="622" width="73" height="55" rx="7"/>
      <rect class="tile" x="745" y="706" width="110" height="57" rx="8"/>
      <rect class="tile" x="710" y="788" width="100" height="56" rx="8"/>
      <rect class="tile" x="597" y="802" width="153" height="86" rx="12"/>
      <rect class="tile" x="773" y="832" width="90" height="58" rx="8"/>
      <rect class="tile" x="620" y="915" width="197" height="112" rx="14"/>
      <rect class="tile" x="620" y="915" width="197" height="112" rx="14"/>
      <rect class="tile" x="244" y="915" width="210" height="118" rx="14"/>
      <rect class="tile" x="412" y="932" width="152" height="86" rx="12"/>
      <rect class="tile" x="536" y="982" width="196" height="110" rx="14"/>
      <rect class="tile" x="705" y="1062" width="160" height="110" rx="14"/>
      <rect class="tile" x="468" y="1048" width="122" height="170" rx="14"/>
      <rect class="tile" x="391" y="1065" width="102" height="58" rx="8"/>
      <rect class="tile--pale" x="208" y="1060" width="155" height="90" rx="12"/>
      <rect class="tile" x="312" y="1093" width="118" height="84" rx="10"/>
      <rect class="tile" x="155" y="1130" width="132" height="90" rx="12"/>
      <rect class="tile" x="617" y="1130" width="122" height="90" rx="12"/>
    </g>

    <path class="tab" d="M0,975 H326 Q341,975 341,990 V1077 Q341,1092 326,1092 H0 Z" fill="var(--orange)"/>
  </svg>

  <header class="brand">
    <div class="brand__name">LIFTOFF</div>
    <div class="brand__tagline">STARTUP HUB</div>
  </header>

  <blockquote class="quote">
    <div class="quote__line line-1"><span class="quote__mark">“</span><span class="quote__small">GREAT</span><span class="quote__large">IDEAS</span></div>
    <div class="quote__line line-2"><span class="quote__small">NEED</span><span class="quote__large">LANDING</span></div>
    <div class="quote__line line-3"><span class="quote__mid">GEAR AS WELL AS</span></div>
    <div class="quote__line line-4"><span class="quote__hero">WINGS</span><span class="quote__mark">”</span></div>
  </blockquote>

  <p class="attribution">E. M. HARLOWE<br>(1902–1964)</p>
</main>
</body>
</html>
```